New Flyer Design Project

To design a sales brochure for our Aloe Vera Drink
5-6 pages
5 x Flavours in 500ml Bottle and
Original, Strawberry, Hawaiin, Mango, Tropical
( 24 pieces per pack )
1 x Flavour in 1.5L Bottle
( 6 pieces per pack )
Brochure to be targeted to Wholesale companies and distributors.

Artwork attached is some artwork , needs a refresh but as the bottle are already made then we cannot change too much .
Some more files available for all flavors.

Brochure Content to be update later

```html
<!DOCTYPE html>
<html lang="en">
<head>
<meta charset="utf-8">
<title>Aloevera Drink – Strawberry Flavor Brochure Spread</title>
<link rel="stylesheet" href="https://fonts.googleapis.com/css2?family=Montserrat:wght@300;400;500;600;700&display=swap">
<style>
  :root {
    --backdrop: #dcdcdc;
    --magenta-deep: #b62a66;
    --magenta: #d13c72;
    --rose: #e56a8f;
    --rose-light: #f39ab4;
    --white: #ffffff;
    --blush: #f7b3c6;
    --leaf: #4fae2e;
    --row-fill: rgba(255, 190, 180, 0.55);
    --gutter-shade: rgba(90, 10, 50, 0.28);
  }
  * { box-sizing: border-box; margin: 0; padding: 0; }
  html, body {
    width: 1200px; height: 800px; overflow: hidden;
    background: var(--backdrop);
    font-family: "Montserrat", sans-serif;
    color: var(--white);
  }
  .spread {
    position: absolute; left: 60px; top: 20px;
    width: 1080px; height: 760px;
    display: flex;
  }
  .page {
    position: relative; width: 540px; height: 760px; overflow: hidden;
  }
  .page--cover {
    background:
      linear-gradient(90deg, transparent 85%, var(--gutter-shade) 100%),
      radial-gradient(ellipse at 40% 75%, var(--rose) 0%, var(--magenta) 50%, var(--magenta-deep) 100%);
  }
  .page--detail {
    background:
      linear-gradient(90deg, var(--gutter-shade) 0%, transparent 12%),
      radial-gradient(ellipse at 45% 55%, var(--rose-light) 0%, var(--rose) 30%, var(--magenta) 65%, var(--magenta-deep) 100%);
  }
  .artwork {
    position: absolute; border-radius: 20px;
  }
  .artwork--hero {
    left: 80px; top: 150px; width: 390px; height: 400px;
    background: radial-gradient(ellipse at 50% 55%, #e8304a 0%, #c8203e 45%, rgba(70,160,60,0.55) 80%, transparent 100%);
  }
  .artwork--bottles {
    left: 60px; top: 330px; width: 210px; height: 250px;
    background: linear-gradient(160deg, #e23a4a 0%, #c9243f 60%, rgba(210,60,80,0.4) 100%);
  }
  .artwork--fruit {
    left: 320px; top: 30px; width: 190px; height: 330px;
    background: linear-gradient(180deg, #d8283c 0%, #c83a50 45%, #4d9c34 75%, rgba(60,140,50,0.3) 100%);
  }
  .cover-title {
    position: absolute; left: 0; right: 40px; bottom: 70px;
    display: flex; align-items: center; gap: 18px;
  }
  .cover-title__rule { width: 80px; height: 4px; background: var(--white); }
  .cover-title__text {
    font-weight: 600; font-size: 52px; letter-spacing: 2px; line-height: 1;
  }
  .cover-subtitle {
    position: absolute; right: 40px; bottom: 40px;
    font-weight: 400; font-size: 18px; color: var(--blush);
  }
  .detail-heading {
    position: absolute; left: 36px; top: 40px;
  }
  .detail-heading__title {
    font-weight: 600; font-size: 26px; letter-spacing: 1px;
  }
  .detail-heading__band {
    display: inline-block; margin-top: 6px;
    background: var(--leaf); padding: 4px 18px 4px 10px;
    font-weight: 400; font-size: 18px;
  }
  .detail-body {
    position: absolute; left: 36px; top: 124px; width: 270px;
    font-size: 11px; line-height: 1.5; font-weight: 400;
  }
  .spec-table {
    position: absolute; border-collapse: collapse;
    font-size: 11px; font-weight: 400;
  }
  .spec-table--sizes { left: 36px; top: 620px; width: 290px; }
  .spec-table--sizes td { padding: 5px 8px; border-top: 1px solid rgba(255,255,255,0.7); }
  .spec-table--sizes td + td { border-left: 1px solid rgba(255,255,255,0.7); }
  .spec-table--sizes tr.is-shaded td { background: var(--row-fill); }
  .spec-block { position: absolute; left: 330px; top: 560px; width: 190px; }
  .spec-block__title {
    font-weight: 300; font-size: 16px; color: var(--blush);
    text-align: right; margin-bottom: 6px;
  }
  .spec-table--carton { position: static; width: 100%; text-align: center; }
  .spec-table--carton th {
    background: var(--row-fill); font-weight: 400; font-size: 10px;
    padding: 4px 3px; line-height: 1.2;
  }
  .spec-table--carton th + th, .spec-table--carton td + td { border-left: 1px solid rgba(255,255,255,0.7); }
  .spec-table--carton td { padding: 5px; border-bottom: 1px solid rgba(255,255,255,0.7); }
</style>
</head>
<body>
  <main class="spread">
    <section class="page page--cover">
      <div class="artwork artwork--hero" role="img" aria-label="Two strawberry aloe vera drink bottles with strawberries, aloe leaves and a juice splash"></div>
      <div class="cover-title">
        <span class="cover-title__rule"></span>
        <h1 class="cover-title__text">ALOEVERA DRINK</h1>
      </div>
      <p class="cover-subtitle">Strawberry Flavor</p>
    </section>

    <section class="page page--detail">
      <header class="detail-heading">
        <h2 class="detail-heading__title">ALOEVERA DRINK</h2>
        <p class="detail-heading__band">Strawberry Flavor</p>
      </header>
      <p class="detail-body">An Exotic and refreshing drink bringing the original taste of Real Aloe Vera Juice and Pulp (40%) infused with tropical flavours. Made with Steviol glycosides extracted from Stevia Plant. Our drink contains 100% of your recommended intake of Vitamin C (per bottle) and we carefully harvest our Aloe Vera ensuring No Aloin. No artificial Colours &amp; No artificial Preservatives</p>
      <div class="artwork artwork--bottles" role="img" aria-label="Two strawberry aloe vera drink bottles"></div>
      <div class="artwork artwork--fruit" role="img" aria-label="Falling strawberries with juice splash above an aloe vera plant"></div>

      <table class="spec-table spec-table--sizes">
        <tr><td>500 ml Mango Flavor Bottle</td><td>12 in pack</td></tr>
        <tr class="is-shaded"><td>1.5 Liter Mango Flavor Bottle</td><td>6 in pack</td></tr>
      </table>

      <div class="spec-block">
        <p class="spec-block__title">Strawberry Flavor</p>
        <table class="spec-table spec-table--carton">
          <tr><th>Quantity per pack</th><th>Quantity per carton</th><th>Quantity per pack</th></tr>
          <tr><td>12</td><td>6</td><td>12</td></tr>
        </table>
      </div>
    </section>
  </main>
</body>
</html>
```